Hip surgeon needs a stationery design

I need a new stationery design for my private practice.
My practice is focused in hip arthroplasty (hip prosthesis).
I'd like to see designs most in blue or shades of blue.
I've uploaded my new logo to help with the task.
Also, I'm a member of some societies and I've uploaded their logos either, so I'd like to see them in some of the stationeries.
Itens list:
business card
letterhead A4
envelope
prescription block A5
one fold for A4 (please see the archive "pocket")
Personal data:
Dr. Renan L. Vasconti
CRM/PR 57316
site: www.clinicapelvora.com.br
email: dr.renan@clinicapelvora.com.br
Adress:
Rua Leopoldo Marques Vieira de Lima, 712
Campo Sereno - Curitiba/PR
41 30875316 I 30875317
Updates
I forgot to mention that my practice is focused primarily in hip arthroplasty (total hip prosthesis) and the target audience range from young adults to the elderly.
I also perform hip preserving surgeries (open and arthroscopic procedures) and pelvic and hip fracture surgery (trauma).
- Any "cleaner" fonts are welcome

```html
<!DOCTYPE html>
<html lang="pt-BR">
<head>
<meta charset="utf-8">
<title>Dr. Renan L. Vasconti — Pasta</title>
<link href="https://fonts.googleapis.com/css2?family=Roboto:wght@300;400;500&display=swap" rel="stylesheet">
<style>
  :root {
    --backdrop: #e8e8e8;
    --paper: #ffffff;
    --paper-shade: #f4f5f6;
    --brand-blue: #1a8fd6;
    --deep-blue: #0f6fbf;
    --sky-blue: #2aa6e6;
    --wash-blue: #dbeaf4;
    --ink-grey: #6f7479;
    --badge-grey: #c9ccd0;
    --badge-green: #b9d98a;
  }
  * { box-sizing: border-box; margin: 0; padding: 0; }
  html, body {
    width: 1200px; height: 847px; overflow: hidden;
    background: var(--backdrop);
    font-family: "Roboto", Arial, sans-serif;
  }
  .folder-spread {
    position: absolute; left: 180px; top: 126px;
    width: 840px; height: 594px;
    display: flex;
    box-shadow: 0 10px 30px rgba(0,0,0,.12);
  }
  .folder-panel {
    position: relative; width: 420px; height: 594px;
    background: var(--paper); overflow: hidden;
  }
  .folder-panel--back {
    background: linear-gradient(90deg, var(--paper) 0%, var(--paper) 80%, var(--paper-shade) 100%);
  }
  .contact-block {
    position: absolute; left: 34px; bottom: 40px;
    list-style: none; color: var(--ink-grey);
    font-size: 7px; line-height: 9.5px; font-weight: 400;
  }
  .contact-block li { display: flex; align-items: flex-start; gap: 6px; }
  .contact-block li + li { margin-top: 1px; }
  .contact-block .address { margin-bottom: 3px; }
  .contact-icon { width: 7px; height: 7px; flex: none; margin-top: 1px; fill: var(--sky-blue); }

  .front-wash { position: absolute; inset: 0; }
  .brand-lockup {
    position: absolute; left: 152px; top: 160px;
    display: flex; align-items: center; gap: 7px;
    color: var(--brand-blue); font-weight: 400;
  }
  .brand-dot { width: 26px; height: 26px; border-radius: 50%; background: var(--brand-blue); flex: none; }
  .brand-name { font-size: 17px; line-height: 19px; letter-spacing: -.2px; }
  .brand-tagline { font-size: 13px; line-height: 15px; }
  .member-row {
    position: absolute; right: 20px; bottom: 24px;
    display: flex; align-items: flex-end; gap: 8px;
  }
  .member-label {
    position: absolute; left: 0; top: -9px;
    font-size: 6px; font-weight: 500; color: var(--deep-blue);
  }
  .member-badge { height: 16px; border-radius: 2px; }
  .member-badge--a { width: 34px; background: var(--badge-green); }
  .member-badge--b { width: 34px; background: var(--badge-grey); }
  .member-badge--c { width: 44px; background: var(--badge-grey); }
  .front-band { position: absolute; left: 0; bottom: 0; width: 420px; height: 20px; }
</style>
</head>
<body>
  <main class="folder-spread">
    <section class="folder-panel folder-panel--back" aria-label="Verso da pasta">
      <ul class="contact-block">
        <li class="address">
          <svg class="contact-icon" viewBox="0 0 10 10"><path d="M5 0a3.5 3.5 0 0 1 3.5 3.5C8.5 6 5 10 5 10S1.5 6 1.5 3.5A3.5 3.5 0 0 1 5 0zm0 2a1.5 1.5 0 1 0 0 3 1.5 1.5 0 0 0 0-3z"/></svg>
          <span>Rua Leopoldo Marques Vieira de Lima,<br>712 Campo Sereno - Curitiba/PR</span>
        </li>
        <li>
          <svg class="contact-icon" viewBox="0 0 10 10"><path d="M2 0l2 2.5-1 1.2a6 6 0 0 0 3.3 3.3l1.2-1L10 8 8.5 10C4 9.5.5 6 0 1.5z"/></svg>
          <span>41 30875316 I 30875317</span>
        </li>
        <li>
          <svg class="contact-icon" viewBox="0 0 10 10"><path d="M0 2h10v6H0zm1 1l4 3 4-3v-.2H1z"/></svg>
          <span>dr.renan@clinicapelvora.com.br</span>
        </li>
        <li>
          <svg class="contact-icon" viewBox="0 0 10 10"><circle cx="5" cy="5" r="4.3" fill="none" stroke="#2aa6e6" stroke-width="1.2"/><path d="M.7 5h8.6M5 .7c2.4 2.4 2.4 6.2 0 8.6M5 .7c-2.4 2.4-2.4 6.2 0 8.6" fill="none" stroke="#2aa6e6" stroke-width=".8"/></svg>
          <span>www.clinicapelvora.com.br</span>
        </li>
      </ul>
    </section>

    <section class="folder-panel folder-panel--front" aria-label="Capa da pasta">
      <svg class="front-wash" viewBox="0 0 420 594" role="img" aria-label="Área decorativa em tons claros de azul">
        <defs>
          <radialGradient id="washGlow" cx="55%" cy="45%" r="70%">
            <stop offset="0" stop-color="#ffffff"/>
            <stop offset=".6" stop-color="#f2f8fc"/>
            <stop offset="1" stop-color="#dbeaf4"/>
          </radialGradient>
        </defs>
        <rect width="420" height="594" fill="url(#washGlow)"/>
      </svg>

      <div class="brand-lockup">
        <span class="brand-dot" aria-hidden="true"></span>
        <div>
          <p class="brand-name">Dr. Renan L. Vasconti</p>
          <p class="brand-tagline">Cirurgia do Quadril</p>
        </div>
      </div>

      <div class="member-row">
        <span class="member-label">Member:</span>
        <span class="member-badge member-badge--a"></span>
        <span class="member-badge member-badge--b"></span>
        <span class="member-badge member-badge--c"></span>
      </div>

      <svg class="front-band" viewBox="0 0 420 20" preserveAspectRatio="none" aria-hidden="true">
        <path d="M0 12 Q200 6 340 8 L340 20 L0 20 Z" fill="var(--deep-blue)"/>
        <path d="M344 8 Q385 6 420 3 L420 20 L344 20 Z" fill="var(--sky-blue)"/>
      </svg>
    </section>
  </main>
</body>
</html>
```